Etiketten-Design für Wasseraufbereiter
Zielgruppe
OBRALU ent­wi­ckelt und pro­du­ziert Pro­duk­te zur Re­gen­was­ser­nut­zung und -ver­si­cke­rung sowie zur Was­ser­auf­be­rei­tung und Grau­was­ser­nut­zung. In unserem Marktsegment zählen wir zu den innovativen und führenden Herstellern. Die Pro­duk­te werden welt­weit über ein wach­sen­des Part­ner- und Händ­ler­netz vertrieben.
Aufgabenstellung
Seit 1993 beschäftigen wir uns mit der Wasseraufbereitung und -wiederverwendung, sowie Regenwasser-Management - also Versickerung und Rückhaltung von Regenwasser. Seit 2016 brauen wir unser exklusives Regenwasserbier. Die Idee mit Regenwasser zu brauen entstand mit einem Partner aus der USA der Hobby „Craft Beer“ Brauer ist. Mit unserer neuen VENTRIX Technologie ist es möglich Regenwasser so aufzubereiten das man es trinken kann also entweder aus dem Wasserahn oder als Bier.
Um es potentiellen Kunden schmackhafter zu machen entschieden wir uns also ein Bier brauen zu lassen. Unsere Grenznähe zu Belgien, einem kleinen Land mit großer Biertrandition, fanden wir eine kleine Brauerei die unser Bier aus Regenwasser im Auftrag und nach eigenem Rezept braut.
Die 0.33l-Flasche (Stuppi) ist Braun. Für die Abmessungen orientiert ihr euch bitte an das Etikett der Hausmarke der Brauerei im Anhang. Es soll ein Bauchetiketten und ein Rückenetikett geben. Bezüglich des Formats, der Größe und der Art des Papiers lassen wir uns gerne durch euch inspirieren. Die maximalen Masse sind jedoch ca. 75mm (B) x ca. 80mm (H). Auf dem Etikett müssen folgende Daten enthalten sein:
- mind. haltbar bis: 12.2023
- ca 6,5% Vol.
- kolmotalbraeu.com
- Sorte (Helles / braun / Spezial)
- Gebraut und abgefüllt in der Kleinbrauerei www.haselmoor-kellerei.beer
- Zutaten: Gerstenmalz, Hopfen, CONTAINS BARLEY MALT, GLUTEN
- 33cl
Von den bestehenden Etiketten ist lediglich der Biername zu übernehmen B= Beer rain_ = regen => Kolmo, zudem sollte der Bezug zum „Regenwasser“ hergestellt werden
Grundsätzlich sind wir sehr offen was die Gestaltung anbelangt und lassen uns gerne durch eure Kreativität überraschen. Da wir eher modern und schlicht, aber auch frisch, witzig und durchaus etwas frech erscheinen möchten, sind traditionelle Bier-Symbole wie Burgen, Mönche oder Getreideähren nicht unser Ding… . ..

```html
<!DOCTYPE html>
<html lang="de">
<head>
<meta charset="utf-8">
<title>Kolmo – Regenwasserbier Etiketten</title>
<link rel="stylesheet" href="https://fonts.googleapis.com/css2?family=Archivo+Black&family=Didact+Gothic&display=swap">
<style>
  :root {
    --canvas: #ececec;
    --label: #1d1d1d;
    --ink: #f2f2f2;
    --muted: #8a8a8a;
    --brune: #b5503f;
    --orge: #f2ad2b;
    --rain-dark: #242424;
  }
  * { box-sizing: border-box; margin: 0; padding: 0; }
  html, body { width: 1200px; height: 900px; overflow: hidden; }
  body {
    background: var(--canvas);
    font-family: "Didact Gothic", "Helvetica Neue", Arial, sans-serif;
    color: var(--ink);
  }
  .label-sheet {
    position: absolute; inset: 0;
    display: grid;
    grid-template-columns: 360px 480px;
    grid-template-rows: 410px 410px;
    gap: 30px 40px;
    justify-content: center;
    align-content: center;
  }
  .label {
    position: relative;
    background: var(--label);
    overflow: hidden;
    box-shadow: 0 2px 10px rgba(0,0,0,.18);
  }
  .variety-brune { --accent: var(--brune); }
  .variety-orge  { --accent: var(--orge); }

  /* Front label */
  .front .wordmark {
    position: absolute; left: 22px; top: 78px;
    font-family: "Archivo Black", "Arial Black", sans-serif;
    font-size: 80px; line-height: 1; letter-spacing: 1px;
    color: var(--ink); text-transform: uppercase;
  }
  .front .variety-name {
    position: absolute; left: 24px; top: 166px;
    font-size: 13px; color: var(--accent);
    font-variant: small-caps;
  }
  .front .rain-scene {
    position: absolute; left: 120px; right: 40px; top: 170px; bottom: 22px;
    background: linear-gradient(180deg, var(--rain-dark) 0%, rgba(255,255,255,.10) 70%, rgba(255,255,255,.22) 100%),
                linear-gradient(90deg, transparent, color-mix(in srgb, var(--accent) 25%, transparent), transparent);
  }
  .front .tagline {
    position: absolute; left: 24px; bottom: 24px;
    font-size: 12px; color: var(--muted); font-variant: small-caps;
  }

  /* Back label */
  .back .rain-strip {
    position: absolute; left: 0; top: 0; width: 110px; height: 250px;
    background: linear-gradient(180deg, rgba(255,255,255,.18), var(--rain-dark) 80%),
                linear-gradient(90deg, transparent, color-mix(in srgb, var(--accent) 30%, transparent));
  }
  .back .figure-mark {
    position: absolute; left: 80px; top: 200px; width: 40px; height: 60px;
    background: linear-gradient(180deg, #dcdcdc, #9a9a9a);
    opacity: .8;
  }
  .back .variety-tag {
    position: absolute; left: 18px; top: 268px; width: 120px; height: 118px;
    background: var(--accent);
    clip-path: polygon(0 0, 100% 0, 78% 100%, 0 100%);
    color: #1a1a1a; padding: 6px 8px;
  }
  .variety-tag .tag-name {
    display: block;
    font-family: "Archivo Black", "Arial Black", sans-serif;
    font-size: 24px; line-height: 1.05;
  }
  .variety-tag .tag-line {
    display: block; font-size: 12px; line-height: 1.2; font-variant: small-caps;
  }
  .variety-tag .tag-sub { opacity: .6; }
  .variety-tag .volume {
    position: absolute; left: 8px; bottom: 8px; font-size: 15px;
  }
  .back .description {
    position: absolute; right: 18px; top: 30px; width: 310px;
    text-align: right; font-size: 11.5px; line-height: 1.42;
  }
  .description p + p { margin-top: 14px; }
  .back .facts {
    position: absolute; right: 18px; bottom: 18px; width: 320px;
    text-align: right; font-size: 10px; line-height: 1.5; font-variant: small-caps;
  }
  .facts .lead { font-size: 11px; }
</style>
</head>
<body>
<main class="label-sheet">

  <section class="label front variety-brune" aria-label="Bauchetikett Kolmo brune">
    <h1 class="wordmark">Kolmo</h1>
    <p class="variety-name">Kolmo brune</p>
    <div class="rain-scene" role="img" aria-label="Illustration: Regenstreifen in Weiß und Rotbraun, Mann mit Regenschirm und Schatten"></div>
    <p class="tagline">Rainwater Beer</p>
  </section>

  <section class="label back variety-brune" aria-label="Rückenetikett Kolmo brune">
    <div class="rain-strip" role="img" aria-label="Illustration: Regenstreifen"></div>
    <div class="figure-mark" role="img" aria-label="Illustration: Figur mit Regenschirm"></div>
    <div class="variety-tag">
      <span class="tag-name">Kolmo</span>
      <span class="tag-line">Kolmo brune</span>
      <span class="tag-line tag-sub">Rainwater Beer</span>
      <span class="volume">℮ 33cl</span>
    </div>
    <div class="description">
      <p>„Kolmo brune“ das dunkle Bier aus Regenwasser</p>
      <p>Das neue Kolmo brune mit 6 % Alkohol hat eine tiefbraune Farbe mit rubinroten Reflexen. Der erste Geschmack ist intensiv und ausgewogen zwischen Bitterheit und dem Geschmack der verschiedenen Malze. Der Nachmund gibt der Süße, die durch das Vorhandensein der Gewürze gekennzeichnet ist, einen Platz und verlangt nach einem weiteren Schluck!</p>
    </div>
    <div class="facts">
      <div>mind. haltbar bis: 12.2023</div>
      <div>ca 6% Vol.</div>
      <div>kolmotalbraeu.com</div>
      <div class="lead">Sorte (Helles / braun / Spezial)</div>
      <div class="lead">Gebraut und abgefüllt in der Kleinbrauerei www.haselmoor-kellerei.beer</div>
      <div class="lead">Zutaten: Gerstenmalz, Hopfen, CONTAINS BARLEY MALT, GLUTEN</div>
    </div>
  </section>

  <section class="label front variety-orge" aria-label="Bauchetikett Kolmo Orge Dorée">
    <h1 class="wordmark">Kolmo</h1>
    <p class="variety-name">Orge Dorée</p>
    <div class="rain-scene" role="img" aria-label="Illustration: Regenstreifen in Weiß und Gelb, Mann mit Regenschirm und Schatten"></div>
    <p class="tagline">Rainwater Beer</p>
  </section>

  <section class="label back variety-orge" aria-label="Rückenetikett Kolmo Orge Dorée">
    <div class="rain-strip" role="img" aria-label="Illustration: Regenstreifen"></div>
    <div class="figure-mark" role="img" aria-label="Illustration: Figur mit Regenschirm"></div>
    <div class="variety-tag">
      <span class="tag-name">Kolmo</span>
      <span class="tag-line">Orge Dorée</span>
      <span class="tag-line tag-sub">Rainwater Beer</span>
      <span class="volume">℮ 33cl</span>
    </div>
    <div class="description">
      <p>Die Brasserie "Orge Dorée" und OBRALU brauen aus Regenwasser ein exklusives Kolmo</p>
      <p>Hopfen, Malz, Hefe und nicht zuletzt Wasser - Bier ist im 500. Jahr des Reinheitsgebots in aller Munde. Eine wachsende Craft-Beer-Bewegung braut mit Begeisterung Biere mit großer geschmacklicher Bandbreite und unverwechselbaren Aromen. Hopfen, Malz und Hefe werden auf kreative Weise zusammengebracht, um Neues zu entwickeln. Der vierte Faktor für ein gutes Bier ist Wasser. Brauereien verfügen meist über eigene, streng gehütete Wasserquellen, um ihr unverwechselbares Bier zu brauen.</p>
    </div>
    <div class="facts">
      <div>mind. haltbar bis: 12.2023</div>
      <div>ca 6,5% Vol.</div>
      <div>kolmotalbraeu.com</div>
      <div class="lead">Sorte (Helles / braun / Spezial)</div>
      <div class="lead">Gebraut und abgefüllt in der Kleinbrauerei www.haselmoor-kellerei.beer</div>
      <div class="lead">Zutaten: Gerstenmalz, Hopfen, CONTAINS BARLEY MALT, GLUTEN</div>
    </div>
  </section>

</main>
</body>
</html>
```